Dorvane Ag Solutions, LLC

Sales, Service, and Repair of Grain Bins

Must include: Insured

Industry/Entity Type

Sales

Contact Information for Business Card

We would like the submitted file to be used in making the business card. Either shrinking it down to use as a "logo" in the left hand side or use it as a back drop with writing over top of it. Would like to have on card also is a name and number: Tom Dorvane (555) 268-3172

Font styles to use
Serif

Requirements
Must have
• Name of owner: Tom Dorvane phone number: 555 268 3172. Free estimates
Nice to have
• Simple and neat design, needs to have the word insured somewhere on the card

```html
<!DOCTYPE html>
<html lang="en">
<head>
<meta charset="utf-8">
<title>Dorvane Ag Solutions, LLC – Business Card</title>
<link rel="stylesheet" href="https://fonts.googleapis.com/css2?family=Source+Serif+4:opsz,wght@8..60,400;8..60,600;8..60,700&display=swap">
<style>
  :root {
    --page-bg: #ffffff;
    --card-bg: #ede9e3;
    --ink: #111111;
    --muted-ink: #3a3631;
    --art-tone: #d8d3cb;
  }
  html, body {
    margin: 0;
    padding: 0;
    width: 1200px;
    height: 1033px;
    overflow: hidden;
    background: var(--page-bg);
    font-family: "Source Serif 4", Georgia, "Times New Roman", serif;
    color: var(--ink);
  }
  .card {
    position: absolute;
    left: 176px;
    top: 277px;
    width: 809px;
    height: 463px;
    background: var(--card-bg);
  }
  .owner-name {
    position: absolute;
    left: 52px;
    top: 126px;
    margin: 0;
    font-size: 68px;
    font-weight: 700;
    letter-spacing: -1px;
    line-height: 1;
    white-space: nowrap;
  }
  .contact-list {
    position: absolute;
    left: 52px;
    top: 236px;
    margin: 0;
    padding: 0;
    list-style: none;
  }
  .contact-item {
    display: flex;
    align-items: center;
    height: 36px;
    font-size: 20px;
  }
  .contact-icon {
    width: 28px;
    height: 24px;
    margin-right: 14px;
    flex: none;
  }
  .service-note {
    position: absolute;
    left: 52px;
    top: 326px;
    margin: 0;
    font-size: 17px;
    font-weight: 600;
    letter-spacing: 0.5px;
    color: var(--muted-ink);
  }
  .service-note .divider {
    margin: 0 10px;
  }
  .brand {
    position: absolute;
    left: 458px;
    top: 125px;
    width: 330px;
    text-align: center;
  }
  .brand-art {
    width: 162px;
    height: 118px;
    margin: 0 auto 8px;
    background: radial-gradient(ellipse at center, var(--art-tone) 0%, var(--card-bg) 75%);
  }
  .brand-name {
    margin: 0;
    font-size: 24px;
    font-weight: 600;
    line-height: 1.1;
    white-space: nowrap;
  }
  .brand-tagline {
    margin: 5px 0 0;
    font-size: 13px;
    letter-spacing: 0.8px;
    line-height: 1.2;
    white-space: nowrap;
  }
</style>
</head>
<body>
  <section class="card">
    <h1 class="owner-name">Tom Dorvane</h1>
    <ul class="contact-list">
      <li class="contact-item">
        <svg class="contact-icon" viewBox="0 0 24 24" aria-hidden="true">
          <path fill="currentColor" d="M6.6 2.5c.6-.3 1.3-.1 1.6.5l1.9 3.4c.3.6.2 1.3-.3 1.7L8.3 9.3c1 2.4 3 4.5 5.4 5.6l1.3-1.5c.4-.5 1.1-.6 1.7-.3l3.5 1.8c.6.3.8 1 .6 1.6l-.9 2.6c-.3.9-1.2 1.4-2.1 1.3C9.6 19.6 4.1 14 3.2 6.1c-.1-.9.4-1.8 1.3-2.1z"/>
        </svg>
        <span class="contact-text">(555) 268-3172</span>
      </li>
      <li class="contact-item">
        <svg class="contact-icon" viewBox="0 0 28 20" aria-hidden="true">
          <rect x="1.5" y="2" width="25" height="16" fill="none" stroke="currentColor" stroke-width="2.6"/>
          <polyline points="2,3 14,12 26,3" fill="none" stroke="currentColor" stroke-width="2.6"/>
        </svg>
        <span class="contact-text">name@email.com</span>
      </li>
    </ul>
    <p class="service-note">Free estimates<span class="divider">•</span>Insured</p>
    <div class="brand">
      <div class="brand-art" role="img" aria-label="Line illustration of two grain bins"></div>
      <p class="brand-name">Dorvane Ag Solutions, LLC</p>
      <p class="brand-tagline">we repair, service, and sales of grain bins</p>
    </div>
  </section>
</body>
</html>
```